Moro Leb Bottling Project needs a Food-Wine Label (front & back) design

We have an approved label for 20L kegs that match with the company name. Now we need to make another label (5 x 3.5 in) more attractive to be used in bottles. We are going to bottling (750ML) wine from kegs. We want to keep, if possible, a relation between both labels, such as the color, appeal to the concept of freshness, directly from the vineyard to your glass, eco-friendly, elegant/ artistic, new way of drinking, the solution or path to the future. We drafted a label with our vision so you can be inspired and complete our idea. Brand is Luz Quieta (still light), varietal and vintage as well as volume are changeable. Company logo is also included for your reference and we would like to be included in the back label or part of it, and also the phrase Moss Wine is another element that we used for our marketing. Any further information contact us.

```html
<!DOCTYPE html>
<html lang="en">
<head>
<meta charset="utf-8">
<title>Luz Quieta Chardonnay – Bottle Labels</title>
<link rel="stylesheet" href="https://fonts.googleapis.com/css2?family=Bebas+Neue&family=Oswald:wght@400;500&family=Montserrat:wght@400;600;700&display=swap">
<style>
  :root{
    --bg:#f4f4f2;
    --front-paper:#eef1cb;
    --back-paper:#ffffff;
    --ink:#3c3c3e;
    --ink-soft:#68686b;
    --pour:#b9d0c4;
    --leaf:#6fae5a;
    --leaf-soft:#a8d39a;
  }
  *{box-sizing:border-box;margin:0;padding:0}
  html,body{width:1200px;height:1200px;overflow:hidden;background:var(--bg)}
  body{font-family:"Montserrat",sans-serif;color:var(--ink);position:relative}

  .label{position:absolute;left:220px;width:760px;height:532px;box-shadow:0 6px 24px rgba(0,0,0,.12)}
  .label--front{top:44px;background:var(--front-paper)}
  .label--back{top:624px;background:var(--back-paper)}

  /* front */
  .brand{position:absolute;left:150px;top:70px;font-family:"Bebas Neue",sans-serif;font-weight:400;color:var(--ink);line-height:.86}
  .brand__top{font-size:170px;letter-spacing:2px;display:block}
  .brand__bottom{font-size:118px;letter-spacing:3px;display:block;color:var(--ink-soft)}
  .pour-art{position:absolute;left:440px;top:40px;width:200px;height:270px}
  .varietal{position:absolute;left:152px;top:312px;font-family:"Oswald",sans-serif;font-weight:500;font-size:34px;letter-spacing:4px;color:var(--ink)}
  .divider{position:absolute;left:150px;top:348px;width:440px;height:40px}
  .vintage{position:absolute;left:154px;top:396px;font-family:"Oswald",sans-serif;font-size:28px;letter-spacing:3px;color:var(--ink)}
  .house-name{position:absolute;left:420px;top:436px;font-family:"Oswald",sans-serif;font-weight:500;font-size:40px;letter-spacing:6px;color:var(--ink-soft);line-height:1}

  /* back */
  .notes{position:absolute;left:60px;top:36px;width:640px;text-align:center;font-size:12.5px;line-height:1.45;color:var(--ink)}
  .notes__title{font-weight:700;font-size:14px;margin-bottom:4px}
  .notes p{font-style:italic}
  .badges{position:absolute;left:60px;top:210px;display:flex;gap:34px;align-items:flex-end}
  .badge{display:flex;flex-direction:column;align-items:center;gap:6px;font-size:10px;letter-spacing:1px}
  .company{display:flex;align-items:center;gap:8px;font-weight:700;font-size:18px;color:var(--ink)}
  .company__mark{width:16px;height:16px;background:var(--ink)}
  .packing{position:absolute;left:400px;top:222px;font-size:12px;font-weight:600;line-height:1.5}
  .warning{position:absolute;left:60px;top:300px;width:640px;font-family:"Oswald",sans-serif;font-size:14px;letter-spacing:.6px;line-height:1.45;text-transform:uppercase;text-align:justify}
  .sulfites{position:absolute;left:60px;top:418px;font-family:"Oswald",sans-serif;font-size:11px;letter-spacing:1px}
  .volume{position:absolute;left:60px;top:432px;font-family:"Bebas Neue",sans-serif;font-size:64px;letter-spacing:1px}
  .abv{position:absolute;left:236px;top:450px;font-family:"Bebas Neue",sans-serif;font-size:38px;letter-spacing:1px}
  .social{position:absolute;left:530px;top:430px;display:flex;flex-direction:column;gap:12px;font-size:14px;font-weight:600}
  .social__item{display:flex;align-items:center;gap:10px}
  .social__dot{width:18px;height:18px;border-radius:50%;background:var(--ink)}
</style>
</head>
<body>

<section class="label label--front" aria-label="Front label">
  <h1 class="brand"><span class="brand__top">LUZ</span><span class="brand__bottom">QUIETA</span></h1>
  <svg class="pour-art" viewBox="0 0 200 270" role="img" aria-label="Illustration of a keg tap pouring into vineyard rows">
    <defs>
      <linearGradient id="pourFade" x1="0" y1="0" x2="0" y2="1">
        <stop offset="0" stop-color="#3c3c3e"/>
        <stop offset=".35" stop-color="#b9d0c4"/>
        <stop offset="1" stop-color="#d4e2c8"/>
      </linearGradient>
    </defs>
    <rect x="0" y="0" width="200" height="270" rx="6" fill="url(#pourFade)" opacity=".55"/>
  </svg>
  <div class="varietal">CHARDONNAY</div>
  <svg class="divider" viewBox="0 0 440 40" aria-hidden="true">
    <path d="M2 34 Q220 6 438 2" fill="none" stroke="#3c3c3e" stroke-width="2"/>
  </svg>
  <div class="vintage">2017</div>
  <div class="house-name">MOSS WINE</div>
</section>

<section class="label label--back" aria-label="Back label">
  <div class="notes">
    <div class="notes__title">2017 Chardonnay – Yakima Valley, WA</div>
    <p>"Aromas of honeysuckle, melon, flowers, toasted cashews... Ripe pears and lemons, crisp fresh acidity expressed in mouth... Elegant subtle creaminess finish with a touch of exotic oak spices... Fermented in stainless-steel followed by a partial malolactic fermentation in French oak barrels, rendering a nicely balanced Chardonnay with great structure, bright and abundant in fruit aromas. Ideal for pairing with poultry (chicken, guinea...), fish (salmon, codfish...) in lightly spiced buttery sauces, creamy pasta dishes, fresh veggie salads and soft-to-mild cheeses. Cheers!"</p>
  </div>

  <div class="badges">
    <div class="badge">
      <svg width="40" height="40" viewBox="0 0 40 40" aria-hidden="true"><circle cx="20" cy="20" r="18" fill="var(--leaf-soft)"/></svg>
      <span>ECO FRIENDLY</span>
    </div>
    <div class="badge">
      <svg width="40" height="40" viewBox="0 0 40 40" aria-hidden="true"><path d="M6 34 C6 14 20 6 36 6 C36 24 26 34 6 34 Z" fill="var(--leaf)"/></svg>
      <span>VEGAN</span>
    </div>
    <div class="company"><span class="company__mark"></span>Moro Leb</div>
  </div>

  <div class="packing">[Packed by ____________, PR ]<br>Distributed by MLBP, Dorado, Puerto Rico</div>

  <p class="warning">Government warning: (1) According to the Surgeon General, women should not drink alcoholic beverages during pregnancy because of the risk of birth defects. (2) Consumption of alcoholic beverages impairs your availability to drive a car or operate machinery, and may cause health problems.</p>

  <div class="sulfites">CONTAIN SULFITES</div>
  <div class="volume">750ML</div>
  <div class="abv">ALC.13.5% BY VOL.</div>

  <div class="social">
    <div class="social__item"><span class="social__dot"></span>@MLBPPR</div>
    <div class="social__item"><span class="social__dot"></span>@mosswine</div>
  </div>
</section>

</body>
</html>
```